Marlowvale Wholefoods web design

Go to marlowvalewholefoods.com.au an using the current layout create a design that will attract customers to this wholefood website.

You may suggest / make slight changes to the layout to create effective graphic design principles.

The LOGO design is TM already. So no changes there. Second logo attached is authorised for use and is a area branding LOGO.

Colours need to reflect health and wellbeing.

Don't want Medical style or New age.
Updates

Thank you for your submissions so far. I have sent them out to a trusty panel of friends to hear what they have to say. Some of you have done very well.

Reason: There are a few submissions outstanding. I will eliminate a few designs today and give feed back. Thankyou

Thank you for your submissions so far I will not be asking for more design submissions from other designers. The ones I have are under consideration and there are a few minor changes to each that may just bring out the one that is IT! The two designs I have narrowed it down to are very different in approach so please bear with me a couple more days. Thank you.

Target Market(s)

Whole food health concious people target market locally Home Delivery would be young Mums with restricted movement because of young children. Older people that are restricted transport users.

Busy commuters that leave our area for work and just want to relax on the weekend with their family and local bush walking or garden activities.

Industry/Entity Type

Graphic Design

Requirements
Should not have
• Medical or sterile hospital feel. New age or too alternative living feel.

```html
<!DOCTYPE html>
<html lang="en">
<head>
<meta charset="utf-8">
<title>Marlowvale Wholefoods</title>
<link href="https://fonts.googleapis.com/css2?family=Open+Sans:wght@400;600;700&display=swap" rel="stylesheet">
<style>
:root{
  --purple:#680f6c;
  --magenta:#a52fa7;
  --green:#5cb543;
  --green-dark:#3f9a2c;
  --pink-bg:#f6e6f3;
  --pink-bar:#efcbeb;
  --price:#c4262e;
  --text:#555;
  --muted:#9a9a9a;
  --blue:#3f8ed6;
}
*{box-sizing:border-box;margin:0;padding:0}
html,body{width:766px;height:1200px;overflow:hidden}
body{position:relative;background:var(--pink-bg);font-family:"Open Sans",sans-serif;color:var(--text)}
.abs{position:absolute}
.topbar{left:0;top:0;width:766px;height:39px;background:var(--purple)}
.navbar{left:0;top:39px;width:766px;height:45px;background:#fff}
.brand{left:64px;top:8px;width:132px;height:68px;border-radius:50%;background:#fff;border:3px solid var(--purple);display:flex;align-items:center;justify-content:center;text-align:center;color:var(--purple);font-weight:700;font-size:12px;line-height:14px}
.cart{left:382px;top:12px;color:#fff;font-weight:600;font-size:11px;display:flex;align-items:center;gap:5px}
.cart-icon{width:19px;height:19px;border-radius:50%;background:#fff;display:flex;align-items:center;justify-content:center}
.search{left:499px;top:10px;width:99px;height:20px;background:#fff;border-radius:2px;font-size:9px;color:#999;padding:4px 8px}
.search svg{position:absolute;right:4px;top:4px}
.btn{top:10px;height:20px;border-radius:2px;color:#fff;font-size:9px;font-weight:600;display:flex;align-items:center;justify-content:center}
.btn-register{left:603px;width:53px;background:var(--blue)}
.btn-login{left:660px;width:42px;background:var(--green)}
.nav{top:54px;font-size:9.5px;color:#666;white-space:nowrap}
.nav.active{color:var(--magenta)}
.panel{left:64px;top:100px;width:638px;height:852px;background:#fff}
.hero{left:70px;top:106px;width:626px;height:240px;background:linear-gradient(90deg,#f7f7f5 0%,#eef0ea 45%,#d8cfc4 70%,#c9d3b6 85%,#eee 100%)}
.hero-kicker{left:94px;top:160px;color:var(--magenta);font-size:19px}
.hero-title{left:92px;top:183px;color:var(--green);font-size:30px;font-weight:600;letter-spacing:.5px}
.hero-copy{left:93px;top:223px;width:240px;font-size:8.5px;line-height:14.5px;color:#555}
.dots{left:93px;top:283px;width:64px;height:14px;border-radius:7px;background:#777;display:flex;align-items:center;justify-content:space-evenly;padding:0 4px}
.dots span{width:7px;height:7px;border-radius:50%;background:#fff}
.dots span:first-child{background:#777;border:1.5px solid #fff}
.section-title{left:70px;color:var(--magenta);font-size:15px}
.more{left:526px;width:9px;height:9px}
.thumb{width:146px;height:85px}
.deal{width:150px;font-size:10px;font-weight:600;line-height:14.5px;color:var(--green)}
.deal b{color:var(--price);font-weight:600}
.rule{left:70px;top:530px;width:466px;height:1px;background:#e6e6e6}
.news-title{font-size:10px;font-weight:600;color:var(--green)}
.news-body{width:148px;font-size:8.2px;line-height:12.2px;color:var(--muted)}
.newsletter{left:550px;top:366px;width:146px;height:116px;background:var(--green)}
.newsletter h3{position:absolute;left:6px;top:6px;color:#fff;font-size:13px;font-weight:600}
.field{position:absolute;left:6px;width:135px;height:20px;background:#fff;font-size:8px;color:#888;padding:5px 8px}
.submit{position:absolute;left:92px;top:87px;width:49px;height:17px;background:#555;color:#fff;font-size:8px;font-weight:600;display:flex;align-items:center;justify-content:center}
.offers{left:550px;top:488px;width:146px;height:141px;background:linear-gradient(160deg,#6e6a62,#b9b2a2 45%,#d9d2c2 70%,#9c957f)}
.offers-title{left:556px;top:494px;color:#fff;font-size:15px;font-weight:600;letter-spacing:.3px}
.cat-bar{left:550px;top:638px;width:146px;height:28px;background:var(--green);color:#fff;font-size:11px;font-weight:600;display:flex;align-items:center;padding-left:6px;gap:6px}
.cats{left:558px;top:676px;list-style:none;font-size:9.4px;color:#555;line-height:20px}
.cats li::before{content:"•";color:#999;margin-right:6px;font-size:7px}
.foot-h{top:983px;color:var(--purple);font-size:11.5px;line-height:14px}
.foot-div{top:982px;width:1px;height:132px;background:#d9bcd5}
.about-copy{left:73px;top:1017px;width:150px;font-size:7.8px;line-height:13.4px;color:#777}
.know{left:73px;top:1086px;font-size:8px;color:#333}
.links{font-size:8.4px;font-weight:600;color:#444;line-height:18.6px;list-style:none}
.links-sm{font-size:7.8px;color:#444;line-height:16px;list-style:none}
.social{left:572px;display:flex;align-items:center;gap:8px;font-size:8px;color:#666}
.social .sq{width:18px;height:18px;background:#6d6d6d;border-radius:2px}
.social em{font-style:normal;font-size:10px;color:#2a64b0}
.bottom{left:0;top:1130px;width:766px;height:70px;background:var(--pink-bar)}
.bottom-links{left:0;top:1148px;width:766px;text-align:center;font-size:8px;color:var(--purple);word-spacing:2px}
.copyright{left:0;top:1171px;width:766px;text-align:center;font-size:8px;color:var(--purple)}
</style>
</head>
<body>
<div class="abs topbar"></div>
<div class="abs navbar"></div>
<div class="abs brand">MARLOWVALE<br>WHOLEFOODS</div>

<div class="abs cart">MY CART - $00.00
  <span class="cart-icon"><svg width="11" height="10" viewBox="0 0 11 10"><path d="M1 3h9l-1 6H2z" fill="#333"/><path d="M3 3l2-2.5M8 3L6 .5" stroke="#333" fill="none"/></svg></span>
</div>
<div class="abs search">Search<svg width="11" height="11" viewBox="0 0 11 11"><circle cx="4.5" cy="4.5" r="3.3" stroke="#777" stroke-width="1.4" fill="none"/><path d="M7 7l3 3" stroke="#777" stroke-width="1.6"/></svg></div>
<div class="abs btn btn-register">REGISTER</div>
<div class="abs btn btn-login">LOG IN</div>

<div class="abs nav active" style="left:247px">HOME</div>
<div class="abs nav" style="left:299px">ABOUT</div>
<div class="abs nav" style="left:355px">SHOP</div>
<div class="abs nav" style="left:405px">PURCHASE BY WEIGHT</div>
<div class="abs nav" style="left:530px">RECEIPES</div>
<div class="abs nav" style="left:595px">BLOG</div>
<div class="abs nav" style="left:645px">CONTACT US</div>

<div class="abs panel"></div>
<div class="abs hero" role="img" aria-label="Woman eating a fresh garden salad"></div>
<div class="abs hero-kicker">Vivamus eget</div>
<div class="abs hero-title">PRAESENT EROS</div>
<p class="abs hero-copy">Praesent fringilla, nisl a fringilla pretium, mauris ante consectetur sapien, non fermentum sapien metus vitae lorem. Donec vel velit tincidunt diam vestibulum.</p>
<div class="abs dots"><span></span><span></span><span></span><span></span></div>

<h2 class="abs section-title" style="top:364px">Latest Deals</h2>
<svg class="abs more" style="top:370px" viewBox="0 0 10 10"><circle cx="5" cy="5" r="4.3" fill="none" stroke="#444"/><path d="M4 3l3 2-3 2z" fill="#444"/></svg>
<div class="abs thumb" style="left:70px;top:393px;background:linear-gradient(135deg,#6b3a1e,#c9a06a 55%,#5a2e17)" role="img" aria-label="Bowl of ground peanut butter"></div>
<div class="abs thumb" style="left:230px;top:393px;background:linear-gradient(135deg,#e6e6e6,#d0c8a8 50%,#a9a9a9)" role="img" aria-label="Capsules on a spoon"></div>
<div class="abs thumb" style="left:389px;top:393px;background:linear-gradient(135deg,#d9a45c,#8a5b34 50%,#e2b06c)" role="img" aria-label="Hands holding seeds in a heart shape"></div>
<div class="abs deal" style="left:71px;top:483px">Fresh Ground Peanut Butter 280g - <b>Now $3.30</b></div>
<div class="abs deal" style="left:231px;top:483px;width:120px">Inner Balance Plus 30c - <b>Now $3.30</b></div>
<div class="abs deal" style="left:390px;top:483px">LSA - <b>Now $3.30</b></div>
<div class="abs rule"></div>

<h2 class="abs section-title" style="top:544px">Latest News</h2>
<svg class="abs more" style="top:550px" viewBox="0 0 10 10"><circle cx="5" cy="5" r="4.3" fill="none" stroke="#444"/><path d="M4 3l3 2-3 2z" fill="#444"/></svg>

<div class="abs thumb" style="left:70px;top:573px;background:linear-gradient(135deg,#dfe7e9,#e7c9b5 50%,#f2f2f2)" role="img" aria-label="Hand holding a supplement bottle"></div>
<div class="abs thumb" style="left:230px;top:573px;background:linear-gradient(135deg,#3a3a3a,#b99e8c 50%,#4a4a4a)" role="img" aria-label="Scoop of linseed meal powder"></div>
<div class="abs thumb" style="left:389px;top:573px;background:linear-gradient(135deg,#cfd8bd,#7f9b4d 50%,#b9c79a)" role="img" aria-label="Green wheatgrass powder and juice"></div>
<div class="abs news-title" style="left:71px;top:663px">Home Deliveries</div>
<div class="abs news-title" style="left:231px;top:663px">Bliss Balls with Linseed Meal</div>
<div class="abs news-title" style="left:390px;top:663px">Curabitur eget augue turpis</div>
<p class="abs news-body" style="left:71px;top:682px">Proin malesuada erat sed rutrum hendrerit. Mauris nisi neque, aliquet nec tortor nec, pellentesque gravida elit. Ut vel nibh suscipit, porta nibh vitae, rhoncus turpis.</p>
<p class="abs news-body" style="left:231px;top:682px">Proin malesuada erat sed rutrum hendrerit. Mauris nisi neque, aliquet nec tortor nec, pellentesque gravida elit. Ut vel nibh suscipit, porta nibh vitae, rhoncus turpis.</p>
<p class="abs news-body" style="left:390px;top:682px">Proin malesuada erat sed rutrum hendrerit. Mauris nisi neque, aliquet nec tortor nec, pellentesque gravida elit. Ut vel nibh suscipit, porta nibh vitae, rhoncus turpis.</p>

<div class="abs thumb" style="left:70px;top:766px;background:linear-gradient(135deg,#6b4a2c,#b59a52 50%,#5b3b22)" role="img" aria-label="Wooden spoon of dried seeds"></div>
<div class="abs thumb" style="left:230px;top:766px;background:linear-gradient(135deg,#8f9aa3,#d8dde0 50%,#6d7780)" role="img" aria-label="Food production line"></div>
<div class="abs thumb" style="left:389px;top:766px;background:linear-gradient(135deg,#7a1830,#b43a4a 50%,#4a2a4a)" role="img" aria-label="Berries mixed with capsules"></div>
<div class="abs news-title" style="left:71px;top:856px">History of the almond.</div>
<div class="abs news-title" style="left:231px;top:856px">Courses</div>
<div class="abs news-title" style="left:390px;top:856px">Curabitur eget augue turpis</div>
<p class="abs news-body" style="left:71px;top:875px">Proin malesuada erat sed rutrum hendrerit. Mauris nisi neque, aliquet nec tortor nec, pellentesque gravida elit. Ut vel nibh suscipit, porta nibh vitae, rhoncus turpis.</p>
<p class="abs news-body" style="left:231px;top:875px">Proin malesuada erat sed rutrum hendrerit. Mauris nisi neque, aliquet nec tortor nec, pellentesque gravida elit. Ut vel nibh suscipit, porta nibh vitae, rhoncus turpis.</p>
<p class="abs news-body" style="left:390px;top:875px">Proin malesuada erat sed rutrum hendrerit. Mauris nisi neque, aliquet nec tortor nec, pellentesque gravida elit. Ut vel nibh suscipit, porta nibh vitae, rhoncus turpis.</p>

<div class="abs newsletter">
  <h3>NEWSLETTER SIGNUP</h3>
  <div class="field" style="top:28px">Name</div>
  <div class="field" style="top:55px">E-mail</div>
  <div class="submit">SUBMIT</div>
</div>
<div class="abs offers" role="img" aria-label="Bowls of dried herbs"></div>
<div class="abs offers-title">SPECIAL OFFERS</div>
<div class="abs cat-bar"><svg width="12" height="12" viewBox="0 0 12 12"><rect x=".5" y=".5" width="11" height="11" fill="none" stroke="#fff"/><path d="M6 3v6M3 6h6" stroke="#fff" stroke-width="1.4"/></svg>Product Categories</div>
<ul class="abs cats">
  <li>Alternative goods</li><li>Dairy Free</li><li>Gluten Free</li><li>Grocery</li><li>Health Supplements</li><li>Natural Grocer</li><li>Organic</li><li>Recipes</li><li>Seasonal</li><li>Specials</li><li>Sugar Replacements</li><li>Vegan</li><li>Vegetarian</li>
</ul>

<h4 class="abs foot-h" style="left:73px">About Marlowvale<br>Wholefoods</h4>
<p class="abs about-copy">Cum sociis natoque penatibus et magnis dis parturient montes, nascetur ridiculus mus. Morbi aliquam dui sed erat sollicitudin, vitae porta justo porta. Integer purus dolor.</p>
<div class="abs know">Know more</div>
<div class="abs foot-div" style="left:236px"></div>
<h4 class="abs foot-h" style="left:252px">Latest Content</h4>
<ul class="abs links" style="left:252px;top:1005px">
  <li>Fresh Ground Peanut Butter 700g</li><li>Fresh Ground Peanut Butter 450g</li><li>Fresh Ground Peanut Butter 280g</li><li>Bliss Balls with Linseed Meal</li><li>History of the almond.</li>
</ul>
<div class="abs foot-div" style="left:418px"></div>
<h4 class="abs foot-h" style="left:439px">About Us</h4>
<ul class="abs links-sm" style="left:439px;top:1006px">
  <li>Special Orders</li><li>Newsletter</li><li>Company</li><li>Contact Us</li><li>Privacy</li><li>Product Recall</li>
</ul>
<div class="abs foot-div" style="left:549px"></div>
<h4 class="abs foot-h" style="left:572px">Connect with us</h4>
<div class="abs social" style="top:1011px"><span class="sq"></span>Join with us on <em>Circlebook</em></div>
<div class="abs social" style="top:1037px"><span class="sq"></span>Follow us on <em>Chirper</em></div>
<div class="abs social" style="top:1064px"><span class="sq"></span>Share on <em>Linkwork</em></div>
<div class="abs social" style="top:1091px"><span class="sq"></span>Watch on <em>ViewTube</em></div>

<div class="abs bottom"></div>
<div class="abs bottom-links">Home &nbsp;| &nbsp;About &nbsp;| &nbsp;Shop &nbsp;| &nbsp;Purchase by Weight &nbsp;| &nbsp;Receipes &nbsp;| &nbsp;Blog &nbsp;| &nbsp;Contact us</div>
<div class="abs copyright">Copyright © 2014 &nbsp;MARLOWVALE WHOLEFOODS. &nbsp;All rights reserved.</div>
</body>
</html>
```